Business Card for premium dental clinic

We are a premium dental clinic based in Brasov, Romania with more than 15 year on the market, providing quality dental treatment made by a team of more specialized dentists, working with modern equipment as a solution to beautiful and healthy teeth.

Our current logo for the clinic use 2 square with colors black and gold - dr Merinca - studio, using family fonts Bodoni, Myriad Pro and Segoe Print.
Depending on the printing we used some gold CMYK background or gold foil picture background or a gold gradient.
We want a business card:
- eye catching business card
- distinguished business card
- premium design
- to keep the color scheme of black and gold
- to attract the customers to spent time reading the information
- modern concept

```html
<!DOCTYPE html>
<html lang="en">
<head>
<meta charset="utf-8">
<title>dr Merinca studio – business card</title>
<link href="https://fonts.googleapis.com/css2?family=Lato:wght@400;900&family=Oswald:wght@400&display=swap" rel="stylesheet">
<style>
  :root {
    --stage: #ebe8e3;
    --card-black: #050709;
    --gold: #f0d04a;
    --gold-light: #f8dc5a;
    --gold-deep: #e2a816;
    --text-grey: #c9c9c9;
    --ink: #1b1b1b;
    --white: #ffffff;
  }
  * { margin: 0; padding: 0; box-sizing: border-box; }
  html, body {
    width: 1200px; height: 1023px; overflow: hidden;
    background: var(--stage);
  }
  .canvas { position: relative; width: 1200px; height: 1023px; }

  .card {
    position: absolute; left: 248px; width: 681px; height: 391px;
    background: var(--card-black); overflow: hidden;
    box-shadow: 0 4px 12px rgba(0,0,0,.18);
  }
  .card--front { top: 87px; }
  .card--back { top: 541px; }

  /* front */
  .brand-name {
    position: absolute; left: 34px; top: 112px; width: 264px;
    font-family: "Lato", sans-serif; font-weight: 400;
    color: var(--white); font-size: 48px; line-height: 1.15; text-align: center;
  }
  .divider {
    position: absolute; left: 343px; top: 84px; width: 2px; height: 223px;
    background: var(--gold-deep);
  }
  .contact { position: absolute; left: 378px; top: 78px; font-family: "Lato", sans-serif; }
  .contact__name {
    font-weight: 900; font-size: 35px; color: var(--gold); letter-spacing: .3px; line-height: 1;
  }
  .contact__role { margin-top: 10px; font-size: 18px; color: var(--text-grey); }
  .contact__address { margin-top: 20px; font-size: 18px; line-height: 25px; color: var(--text-grey); }
  .contact__list { list-style: none; margin-top: 16px; }
  .contact__item {
    display: flex; align-items: center; height: 34px;
    font-size: 18px; color: var(--text-grey);
  }
  .contact__icon { width: 18px; height: 18px; margin-right: 16px; flex: none; }

  /* back */
  .gold-panel {
    position: absolute; left: 0; top: 0; width: 342px; height: 100%;
    background: linear-gradient(135deg, var(--gold-light) 0%, var(--gold) 45%, var(--gold-deep) 100%);
  }
  .name-plate {
    position: absolute; left: 38px; top: 124px; width: 304px; height: 141px;
    background: var(--white);
    display: flex; align-items: center; justify-content: center;
  }
  .name-plate__text {
    font-family: "Lato", sans-serif; font-weight: 400;
    font-size: 32px; color: var(--ink);
  }
  .tagline {
    position: absolute; right: 12px; bottom: 14px;
    font-family: "Oswald", sans-serif; font-weight: 400;
    font-size: 46px; line-height: 1; color: var(--white);
  }
</style>
</head>
<body>
<main class="canvas">

  <section class="card card--front" aria-label="Card front">
    <p class="brand-name">dr Merinca<br>studio</p>
    <div class="divider"></div>
    <div class="contact">
      <h1 class="contact__name">ADRIAN PAVEL</h1>
      <p class="contact__role">Managing Director</p>
      <p class="contact__address">2345 First Address Line<br>Second Address Line, 56324</p>
      <ul class="contact__list">
        <li class="contact__item">
          <svg class="contact__icon" viewBox="0 0 24 24" fill="var(--gold)"><path d="M6.6 10.8a15.1 15.1 0 0 0 6.6 6.6l2.2-2.2a1 1 0 0 1 1-.25 11.4 11.4 0 0 0 3.6.57 1 1 0 0 1 1 1V20a1 1 0 0 1-1 1A17 17 0 0 1 3 4a1 1 0 0 1 1-1h3.5a1 1 0 0 1 1 1c0 1.25.2 2.45.57 3.57a1 1 0 0 1-.25 1z"/></svg>
          123 456 7890
        </li>
        <li class="contact__item">
          <svg class="contact__icon" viewBox="0 0 24 24"><rect x="2" y="5" width="20" height="14" fill="var(--gold)"/><path d="M2 5l10 8 10-8M2 19l8-7M22 19l-8-7" stroke="var(--card-black)" stroke-width="1.5" fill="none"/></svg>
          lorem@yourwebsite.com
        </li>
        <li class="contact__item">
          <svg class="contact__icon" viewBox="0 0 24 24" fill="none" stroke="var(--gold)" stroke-width="1.8"><circle cx="12" cy="12" r="10"/><ellipse cx="12" cy="12" rx="4.5" ry="10"/><path d="M2 12h20M4 7h16M4 17h16"/></svg>
          www.yourwebsite.com
        </li>
      </ul>
    </div>
  </section>

  <section class="card card--back" aria-label="Card back">
    <div class="gold-panel" role="img" aria-label="Crumpled gold foil texture"></div>
    <div class="name-plate"><span class="name-plate__text">dr Merinca studio</span></div>
    <p class="tagline">dental clinic</p>
  </section>

</main>
</body>
</html>
```